Financial Services Business Card Design

We are a financial services company Based in London, offering Short term Funding Solutions for companies, raising anywhere between £20,000 and £25million pounds.

The Card must have a professional look as it is going to be handed out to professionals I.E Solicitors, Accountants, Company directors and Business owners.

See Attached our company Logo

Industry/Entity Type

Business

Contact Information for Business Card

Brett Kolvane
Suite 41
R T House
Hazelbrook Lane
Watford
WD17 4QL

```html
<!DOCTYPE html>
<html lang="en">
<head>
<meta charset="utf-8">
<title>Kestrel Bridge Capital — Business Card</title>
<link rel="stylesheet" href="https://fonts.googleapis.com/css2?family=Arimo:wght@400;700&display=swap">
<style>
  :root {
    --backdrop: #e6e7e9;
    --brand-green: #369e34;
    --brand-blue: #1f68b3;
    --card-white: #f6f6f6;
    --text-grey: #6d6f72;
    --ink-white: #ffffff;
  }
  * { box-sizing: border-box; margin: 0; padding: 0; }
  html, body {
    width: 1200px;
    height: 900px;
    overflow: hidden;
    background: var(--backdrop);
    font-family: "Arimo", Arial, sans-serif;
  }
  .sheet {
    position: relative;
    width: 1200px;
    height: 900px;
  }
  .card {
    position: absolute;
    left: 320px;
    width: 560px;
    height: 320px;
    box-shadow: 0 6px 18px rgba(0, 0, 0, 0.12);
  }
  .card--front {
    top: 100px;
    background: var(--brand-green);
    display: flex;
    align-items: center;
    justify-content: center;
  }
  .card--back {
    top: 480px;
    background: var(--card-white);
    display: flex;
    align-items: center;
    padding: 0 48px;
  }
  .brand {
    display: flex;
    align-items: center;
    gap: 12px;
  }
  .brand__dot {
    width: 18px;
    height: 18px;
    border-radius: 50%;
    flex: none;
  }
  .brand__name {
    font-weight: 700;
    text-transform: uppercase;
    letter-spacing: 0.5px;
  }
  .card--front .brand__dot { background: var(--ink-white); }
  .card--front .brand__name {
    color: var(--ink-white);
    font-size: 26px;
  }
  .card--back .brand { width: 270px; }
  .card--back .brand__dot { background: var(--brand-green); }
  .card--back .brand__name {
    color: var(--brand-blue);
    font-size: 22px;
    line-height: 1.15;
  }
  .contact {
    margin-left: 36px;
  }
  .contact__name {
    color: var(--brand-blue);
    font-weight: 700;
    font-size: 17px;
    text-transform: uppercase;
    margin-bottom: 8px;
  }
  .contact__address {
    font-style: normal;
    color: var(--text-grey);
    font-size: 14px;
    line-height: 1.3;
    padding-left: 18px;
  }
</style>
</head>
<body>
  <main class="sheet">
    <section class="card card--front" aria-label="Card front">
      <div class="brand">
        <span class="brand__dot"></span>
        <span class="brand__name">Kestrel Bridge Capital</span>
      </div>
    </section>

    <section class="card card--back" aria-label="Card back">
      <div class="brand">
        <span class="brand__dot"></span>
        <span class="brand__name">Kestrel Bridge<br>Capital</span>
      </div>
      <div class="contact">
        <h1 class="contact__name">Brett Kolvane</h1>
        <address class="contact__address">
          Suite 41<br>
          R T House<br>
          Hazelbrook Lane<br>
          Watford<br>
          WD17 4QL
        </address>
      </div>
    </section>
  </main>
</body>
</html>
```